tralvix

social business web site uniting communities in condominiums, clubs, hotels and the shops outlets nearby resulting in discounts coupons to the members and deal of the day offers in the vicinity of the communities.
the page can be seen at TRALVIX.NET and the logo is seen there in red and blue colors which is to be maintained.
the ultimate idea of this network is to exercise the power of the mobs when applied to any goals either commercial, social, environmental or political and give power to the mobs to let them rule.
we need 2 pages:
front page - home which is currently fixed page but in future will be dynamic with regular feeds and updates. so this condition must be foreseen in the project.
inner page - we hv many pages inside but the same construction, just titled differently.
the winning layout will have to be supplied also in html and css format.

Industry/Entity Type

Political

```html
<!DOCTYPE html>
<html lang="en">
<head>
<meta charset="utf-8">
<title>Tralvix — Home</title>
<link href="https://fonts.googleapis.com/css2?family=Arimo:wght@400;700&display=swap" rel="stylesheet">
<style>
:root{
  --page-bg:#e3e3e3;
  --header-bg:#f4f4f4;
  --skyline:#dcdcdc;
  --white:#ffffff;
  --red:#d42a1f;
  --heading-red:#c8261c;
  --blue:#0f88e2;
  --blue-dark:#0a6fc0;
  --link-blue:#1a6fc8;
  --text:#5d5d5d;
  --text-dark:#3a3a3a;
  --rule:#e2e2e2;
  --frame:#ececec;
  --dot:#bdbdbd;
  --icon:#9c9c9c;
}
*{margin:0;padding:0;box-sizing:border-box}
html,body{width:1150px;height:1200px;overflow:hidden}
body{background:var(--page-bg);font-family:"Arimo",Arial,sans-serif;color:var(--text);position:relative}
.abs{position:absolute}

.site-header{left:0;top:0;width:1150px;height:186px;background:var(--header-bg);border-bottom:3px solid var(--white)}
.skyline{left:0;top:0;width:1150px;height:160px;background:linear-gradient(180deg,#f6f6f6 0%,#e6e6e6 55%,var(--skyline) 100%)}
.brand{left:90px;top:40px;display:flex;align-items:center;gap:12px}
.brand-mark{width:34px;height:34px;border-radius:50%;background:var(--blue)}
.brand-name{font-size:48px;font-weight:700;color:var(--red);letter-spacing:-1px}

.search{left:867px;top:103px;width:198px;height:37px;background:var(--white);border:1px solid #d6d6d6;border-radius:3px;box-shadow:inset 0 1px 3px rgba(0,0,0,.08)}
.search span{position:absolute;left:12px;top:12px;font-size:11px;color:#9a9a9a}
.search svg{position:absolute;right:10px;top:12px}

.main-nav{left:89px;top:161px;width:973px;height:52px;background:linear-gradient(180deg,#1a96ec 0%,var(--blue) 60%,#0b7dd6 100%);display:flex}
.main-nav a{height:52px;line-height:52px;color:var(--white);text-decoration:none;font-size:14px;text-align:center;border-right:1px solid #0a6cb8}
.main-nav a.current{background:linear-gradient(180deg,#e03a2e,#c5261b);border-right:none}

.content{left:85px;top:213px;width:980px;height:902px;background:var(--white)}

.slider{left:91px;top:222px;width:969px;height:290px;background:linear-gradient(90deg,#e2e3e5 0%,#f1f2f3 55%,#e7e8e9 100%);border:3px solid #f2f2f2;box-shadow:0 8px 10px -6px rgba(0,0,0,.25)}
.slider-map{left:40px;top:30px;width:460px;height:110px;border-radius:40px 60px 30px 50px;background:linear-gradient(180deg,#c3c5c9 0%,#cdcfd2 100%)}
.slider-people{left:26px;top:100px;width:484px;height:128px;border-radius:6px;background:linear-gradient(90deg,#7b6651 0%,#a08e8c 13%,#a5472f 26%,#6f8e9a 40%,#8d4f3b 53%,#5e5c72 66%,#a33f36 80%,#5f3f68 100%);opacity:.9}
.slider-text{left:562px;top:95px;width:380px;font-size:18px;line-height:25px;color:var(--text-dark)}
.slider-text .brand-word{color:var(--red)}
.slider-text .accent{color:var(--link-blue)}
.btn{display:block;width:89px;height:28px;line-height:28px;text-align:center;color:var(--white);font-size:12px;border-radius:3px;text-decoration:none}
.btn-dark{background:linear-gradient(180deg,#4a4a4a,#2e2e2e)}
.btn-blue{background:linear-gradient(180deg,#2a8ee0,var(--blue-dark));box-shadow:0 2px 2px rgba(0,0,0,.2)}
.slider .btn{position:absolute;left:562px;top:156px}
.dots{left:864px;top:253px;display:flex;gap:10px}
.dots i{width:11px;height:11px;border-radius:50%;background:var(--dot)}
.dots i.on{background:var(--blue)}

.welcome h1{font-size:20px;font-weight:400;color:var(--heading-red)}
.welcome{left:96px;top:568px;width:684px}
.welcome p{margin-top:14px;font-size:13px;line-height:22px}
.welcome-art{left:790px;top:555px;width:258px;height:145px;border-radius:4px;background:linear-gradient(90deg,#d6e7f5 0%,#6aaee0 40%,#2a77b8 70%,#163a5e 100%)}

.rule{left:95px;top:724px;width:960px;height:1px;background:var(--rule)}

.feature{top:746px;width:297px}
.feature h2{font-size:20px;font-weight:400;color:var(--heading-red);margin-left:2px}
.feature-img{margin-top:16px;width:298px;height:136px;border:5px solid var(--frame)}
.feature p{margin-top:13px;margin-left:2px;font-size:13px;line-height:22px;text-align:justify;hyphens:auto;-webkit-hyphens:auto}
.feature p .accent{color:var(--link-blue)}
.feature .btn{position:absolute;left:2px;top:314px}

.footer-links{left:86px;top:1134px;font-size:12px;color:#6b6b6b}
.footer-links a{color:#6b6b6b;text-decoration:none}
.footer-links b{font-weight:400;margin:0 8px}
.copyright{left:86px;top:1166px;font-size:12px;color:#6b6b6b;word-spacing:2px}
.social{left:941px;top:1145px;display:flex;gap:9px}
.social i{width:24px;height:24px;border-radius:50%;background:var(--icon);display:block}
</style>
</head>
<body>

<header class="site-header abs">
  <div class="skyline abs" role="img" aria-label="Faint city skyline with light rays"></div>
  <div class="brand abs">
    <span class="brand-mark"></span>
    <span class="brand-name">Tralvix</span>
  </div>
  <div class="search abs">
    <span>Search</span>
    <svg width="12" height="12" viewBox="0 0 12 12"><circle cx="5" cy="5" r="3.5" fill="none" stroke="#aaa" stroke-width="1.3"/><line x1="7.6" y1="7.6" x2="11" y2="11" stroke="#aaa" stroke-width="1.5"/></svg>
  </div>
</header>

<nav class="main-nav abs">
  <a class="current" href="#" style="width:97px">Home</a>
  <a href="#" style="width:119px">About us</a>
  <a href="#" style="width:146px">How It Works</a>
  <a href="#" style="width:160px">What is Tralvix</a>
  <a href="#" style="width:130px">Contact Us</a>
  <a href="#" style="width:96px">Login</a>
  <a href="#" style="width:110px">Register</a>
</nav>

<main class="content abs"></main>

<section class="slider abs">
  <div class="slider-map abs" role="img" aria-label="Grey world map"></div>
  <div class="slider-people abs" role="img" aria-label="Row of colourful paper-cut people holding hands"></div>
  <p class="slider-text abs"><span class="brand-word">TRALVIX</span> <span class="accent">is a social network</span> that integrates people and business communities</p>
  <a class="btn btn-dark" href="#">View more</a>
  <div class="dots abs"><i class="on"></i><i></i><i></i><i></i></div>
</section>

<section class="welcome abs">
  <h1>Welcome to our site</h1>
  <p>Cras vehicula ligula a purus tempus interdum. Curabitur est lorem, laoreet eget tincidunt vitae, molestie sed magna. Duis tincidunt lectus in est ultrices semper congue dolor interdum. Donec venenatis sodales tellus, nec interdum lorem iaculis vitae. Praesent quis nunc non lectus egestas fermentum eu nec mauris. Praesent placerat adipiscing euismod. Phasellus arcu ipsum, tempus nec rhoncus in, ultrices et leo.</p>
</section>
<div class="welcome-art abs" role="img" aria-label="Blue silhouettes of a crowd of business people"></div>

<div class="rule abs"></div>

<article class="feature abs" style="left:95px">
  <h2>About us</h2>
  <div class="feature-img" role="img" aria-label="Team of business people standing in an office" style="background:linear-gradient(90deg,#dfe5ea 0%,#dfe5ea 12%,#2b2d33 22%,#44474e 40%,#25272c 55%,#5a5d63 72%,#2a2c31 85%,#e2e7eb 94%)"></div>
  <p>TRALVIX is a social network that integrates people and business communities. With that, it promotes sports, leisure or social in safe environments, like condos where people live, hotels, clubs, restaurants, gyms etc..</p>
  <a class="btn btn-blue" href="#">View more</a>
</article>

<article class="feature abs" style="left:427px">
  <h2>How it works</h2>
  <div class="feature-img" role="img" aria-label="Connected devices: tablet, phone, router, laptop and globe" style="background:linear-gradient(135deg,#f4f7fa 0%,#8fa8bd 30%,#3f5466 50%,#5aa6e0 70%,#1c2430 88%,#f4f7fa 100%)"></div>
  <p>TRALVIX works via socialization of people who live, work, study or are close permanently or temporarily and try to join at any time to the needs of each other. TRALVIX With communities have a voice and its members can listen to it and follow it.</p>
  <a class="btn btn-blue" href="#">View more</a>
</article>

<article class="feature abs" style="left:758px">
  <h2>What is Tralvix?</h2>
  <div class="feature-img" role="img" aria-label="Hand holding a social media sphere" style="background:linear-gradient(180deg,#f2f2f2 0%,#b9b9b9 35%,#6d6d6d 55%,#e7b08a 80%,#f7e2d2 100%)"></div>
  <p>WHAT YOU WANT TRALVIX TRALVIX wants to transform the way we live in communities, bringing more people and generating it with several opportunities. <span class="accent">People in these communities will decide what to do as a community!</span></p>
  <a class="btn btn-blue" href="#">View more</a>
</article>

<footer>
  <div class="footer-links abs">
    <a href="#">Home</a><b>|</b><a href="#">About us</a><b>|</b><a href="#">How It Works</a><b>|</b><a href="#">What is Tralvix</a><b>|</b><a href="#">Contact Us</a><b>|</b><a href="#">Login</a><b>|</b><a href="#">Register</a>
  </div>
  <p class="copyright abs">Copyright &nbsp;©&nbsp; 2013 &nbsp;&nbsp;www.tralvix.net &nbsp;&nbsp;All rights reserved.</p>
  <div class="social abs"><i></i><i></i><i></i><i></i></div>
</footer>

</body>
</html>
```